Local Swedish accounting firm needs a webpage design.

We need a logo design for an accounting firm based in Malmö, Sweden called "Veltrana". We provide a full range of accounting services and have worked closely with startups for many years.
We would like to see an design using the following color scheme.
https://huepiq.io/9b90ba-bfae48-646f58-2541b2-d56501
The design should communicate ease of use and financial safety.

Target Market(s)

We are an accounting firm so are clients are startups and small to medium sized companys

Industry/Entity Type

Accounting

Coding

Coded - Design and coding required

Number of Pages Required

1 page

Font styles to use
Sans Serif

```html
<!DOCTYPE html>
<html lang="en">
<head>
<meta charset="utf-8">
<title>Veltrana – Accounting in Malmö</title>
<link href="https://fonts.googleapis.com/css2?family=Poppins:wght@600;700&family=Roboto:wght@400;500;700&display=swap" rel="stylesheet">
<style>
:root{
  --sky:#dff3f3;
  --purple:#8b7cb0;
  --purple-soft:#9b90ba;
  --gold:#bfae48;
  --olive:#a39c3c;
  --orange:#d56501;
  --sun:#f0a21c;
  --ink:#1e1e1e;
  --text:#4a4a4a;
  --white:#ffffff;
}
*{margin:0;padding:0;box-sizing:border-box}
html,body{width:1200px;height:3444px;overflow:hidden}
body{position:relative;background:var(--white);font-family:"Roboto",Arial,sans-serif;color:var(--text)}
.abs{position:absolute}
.heading{font-family:"Poppins","Roboto",sans-serif;font-weight:700;color:var(--ink)}
.btn{position:absolute;display:flex;align-items:center;justify-content:center;gap:8px;border-radius:22px;font-weight:700;font-size:15px;text-transform:uppercase;letter-spacing:.2px}
.btn-solid{background:var(--orange);color:var(--white)}
.btn-outline{background:var(--white);color:var(--orange);border:2px solid var(--orange)}
.btn svg{width:14px;height:14px}

/* header */
.hero{left:0;top:0;width:1200px;height:760px;background:var(--sky)}
.nav a{position:absolute;top:82px;font-size:15px;font-weight:500;color:var(--ink);text-decoration:none}
.nav a.active{color:var(--sun)}
.brand{position:absolute;left:490px;top:52px;display:flex;align-items:center;gap:10px;font-weight:500;font-size:22px;color:var(--ink)}
.brand i{display:block;width:44px;height:44px;border-radius:50%;background:var(--sun)}
.hero-title{left:0;width:1200px;top:186px;text-align:center;font-size:44px}
.hero-sub{left:0;width:1200px;top:258px;text-align:center;font-size:17px;line-height:27px;font-weight:500;color:#3a3a3a}
.hero-art{left:0;top:374px}

/* about */
.about-title{left:110px;top:846px;font-size:34px}
.about-text{left:110px;top:912px;width:450px;font-size:14px;line-height:25.7px}
.compass{left:640px;top:808px}

/* services */
.services{left:0;top:1250px}
.svc-title{left:0;width:1200px;top:1335px;text-align:center;font-size:40px;color:var(--white)}
.svc-intro{left:150px;width:900px;top:1400px;text-align:center;color:var(--white);font-size:15px;line-height:23px}
.svc{position:absolute;top:1500px;width:230px;text-align:center;color:var(--white)}
.svc .icon{width:96px;height:96px;margin:0 auto;border-radius:50%;background:var(--gold);border:3px solid #d8c866;display:flex;align-items:center;justify-content:center}
.svc h3{margin-top:28px;font-size:18px;font-weight:700;line-height:27px;text-transform:uppercase}
.svc p{margin-top:6px;font-size:14px;line-height:20.5px}
.arrow{top:1654px;width:24px;height:40px}

/* clients */
.clients-title{left:0;width:1200px;top:1953px;text-align:center;font-size:38px}
.card{position:absolute;top:2094px;width:310px;height:191px;border:1px solid #d9d9d9;border-top:2px solid var(--gold);border-radius:10px;background:var(--white)}
.card p{position:absolute;left:26px;right:26px;top:66px;text-align:center;font-size:14px;line-height:25.7px}
.avatar{position:absolute;top:2051px;width:88px;height:88px;border-radius:50%;background:linear-gradient(#c9c4c0,#8f8a86);border:3px solid var(--white)}
.person{position:absolute;top:2305px;width:310px;text-align:center;font-size:15px;font-weight:500;color:var(--ink)}
.person small{font-size:10px;font-weight:400;color:var(--text)}
.stars{position:absolute;top:2331px;width:310px;text-align:center;color:var(--sun);font-size:13px;letter-spacing:1px}

/* quote */
.quote{left:0;top:2430px}
.quote-title{left:110px;top:2620px;font-size:40px;color:var(--white)}
.quote-text{left:112px;top:2694px;width:450px;font-size:15px;line-height:26px;color:var(--white)}
.devices{left:608px;top:2569px;width:374px;height:410px;border-radius:18px;background:linear-gradient(135deg,#2b2b2b,#55524a 60%,#e9e9e9)}

/* footer */
.foot-brand{left:158px;top:3180px;display:flex;align-items:center;gap:10px;font-weight:500;font-size:20px;color:var(--ink)}
.foot-brand i{display:block;width:40px;height:40px;border-radius:50%;background:var(--sun)}
.social{top:3278px;width:32px;height:32px;border-radius:50%}
.foot-head{top:3140px;font-size:16px;font-weight:700;color:var(--ink)}
.links{left:434px;top:3182px;list-style:none;font-size:13.5px;line-height:25.7px}
.contact{left:631px;top:3178px;font-size:13.5px}
.contact .row{position:relative;padding-left:22px;margin-bottom:14px;line-height:17px}
.contact b{display:block;font-size:11.5px;color:var(--ink)}
.contact svg{position:absolute;left:0;top:2px;width:13px;height:13px}
.partner{left:913px;top:3208px;display:flex;align-items:center;gap:10px;font-size:24px;font-weight:400;color:var(--ink)}
.partner i{display:block;width:26px;height:26px;background:#f2c200}
.rule{left:110px;top:3373px;width:980px;height:1px;background:#cfcfcf}
.copyright{left:0;width:1200px;top:3394px;text-align:center;font-size:14.5px}
.to-top{left:1108px;top:3357px;width:32px;height:32px;border-radius:50%;background:var(--gold);display:flex;align-items:center;justify-content:center}
</style>
</head>
<body>

<!-- Header & hero -->
<div class="abs hero"></div>
<nav class="nav">
  <a class="active" href="#" style="left:110px">Home</a>
  <a href="#" style="left:175px">Our services</a>
  <a href="#" style="left:288px">For Entre preneurs</a>
  <a href="#" style="left:793px">About Us</a>
  <a href="#" style="left:879px">GDPR</a>
  <a href="#" style="left:942px">Contact Us</a>
  <a href="#" style="left:1038px">En ⌄</a>
</nav>
<div class="brand"><span>Veltrana</span><i></i></div>
<h1 class="abs heading hero-title">VELTRANA</h1>
<p class="abs hero-sub">If you want to devote yourself wholeheartedly to your business,<br>help with current accounting is good advice.</p>
<a class="btn btn-solid" href="#" style="left:516px;top:335px;width:170px;height:45px">Contact us
  <svg viewBox="0 0 16 16"><circle cx="8" cy="8" r="8" fill="#fff"/><path d="M6 4l4 4-4 4" stroke="#d56501" stroke-width="2" fill="none"/></svg></a>
<svg class="abs hero-art" width="1200" height="386" viewBox="0 0 1200 386" role="img" aria-label="Illustration of a desk with hands working on a laptop, calculator, documents and charts">
  <defs><linearGradient id="desk" x1="0" y1="0" x2="0" y2="1"><stop offset="0" stop-color="#dff3f3"/><stop offset="1" stop-color="#c7dfe3"/></linearGradient></defs>
  <path d="M0 0H1200V210Q900 380 600 382Q300 380 0 280Z" fill="url(#desk)"/>
  <path d="M0 290Q300 385 600 382Q900 378 1200 222" stroke="var(--gold)" stroke-width="7" fill="none"/>
</svg>

<!-- About -->
<h2 class="abs heading about-title">ABOUT US</h2>
<p class="abs about-text">Successful companies know that financial control is a crucial factor. Structure, clear goals and systematic follow-up are the guiding principles on the road to good results. We can provide your company with financial expertise in several areas and create and follow up the routines that keep the course straight towards the goals. You get a partner who with commitment analyzes and gives advice from a holistic perspective.</p>
<a class="btn btn-solid" href="#" style="left:110px;top:1120px;width:145px;height:41px">Read more
  <svg viewBox="0 0 16 16"><circle cx="8" cy="8" r="8" fill="#fff"/><path d="M6 4l4 4-4 4" stroke="#d56501" stroke-width="2" fill="none"/></svg></a>
<svg class="abs compass" width="410" height="400" viewBox="0 0 410 400" role="img" aria-label="Large decorative emblem area">
  <circle cx="205" cy="200" r="160" fill="#fdf1da"/>
</svg>

<!-- Services -->
<svg class="abs services" width="1200" height="665" viewBox="0 0 1200 665">
  <path d="M0 86L600 6L1200 86V660L600 588L0 660Z" fill="var(--purple)"/>
  <path d="M0 86L600 6L1200 86" stroke="var(--gold)" stroke-width="8" fill="none"/>
</svg>
<h2 class="abs heading svc-title">WHAT WE DO</h2>
<p class="abs svc-intro">Lorem ipsum dolor sit amet, consectetur adipiscing elit, sed do eiusmod tempor incididunt ut labore et dolore magna aliqua. Ut enim ad minim veniam, quis nostrud exercitation ullamco laboris nisi ut aliquip ex ea commodo consequat. Duis aute irure dolor in reprehenderit in voluptate velit esse cillum dolore eu fugiat nulla pariatur.</p>

<div class="svc" style="left:108px">
  <div class="icon"><svg width="40" height="40" viewBox="0 0 40 40" fill="none" stroke="#fff" stroke-width="2"><rect x="8" y="5" width="24" height="30" rx="2"/><path d="M13 13h14M13 19h14M13 25h9"/></svg></div>
  <h3>Accounting</h3>
  <p>Lorem ipsum dolor sit consectetur adipiscing elit, sed do eiusmod tempor incididunt labore et dolore magna aliqua.</p>
</div>
<div class="svc" style="left:359px">
  <div class="icon"><svg width="40" height="40" viewBox="0 0 40 40" fill="none" stroke="#fff" stroke-width="2"><rect x="6" y="10" width="28" height="22" rx="2"/><circle cx="20" cy="21" r="5"/><path d="M14 6h12"/></svg></div>
  <h3>Payroll management</h3>
  <p>Lorem ipsum dolor sit consectetur adipiscing elit, sed do eiusmod tempor incididunt labore et dolore magna aliqua.</p>
</div>
<div class="svc" style="left:610px">
  <div class="icon"><svg width="40" height="40" viewBox="0 0 40 40" fill="none" stroke="#fff" stroke-width="2"><rect x="7" y="5" width="20" height="28" rx="2"/><circle cx="26" cy="27" r="6"/><path d="M11 11h12M11 17h12"/></svg></div>
  <h3>Annual accounts and declarations</h3>
  <p>Lorem ipsum dolor sit consectetur adipiscing elit, sed do eiusmod tempor incididunt</p>
</div>
<div class="svc" style="left:862px">
  <div class="icon"><svg width="40" height="40" viewBox="0 0 40 40" fill="none" stroke="#fff" stroke-width="2"><rect x="6" y="7" width="22" height="26" rx="2"/><rect x="20" y="18" width="14" height="16" rx="2"/><path d="M10 13h12"/></svg></div>
  <h3>Project accounting</h3>
  <p>Lorem ipsum dolor sit consectetur adipiscing elit, sed do eiusmod tempor incididunt labore et dolore magna aliqua.</p>
</div>

<a class="btn btn-solid" href="#" style="left:144px;top:1754px;width:160px;height:41px">Learn more <svg viewBox="0 0 16 16"><circle cx="8" cy="8" r="8" fill="#fff"/><path d="M6 4l4 4-4 4" stroke="#d56501" stroke-width="2" fill="none"/></svg></a>
<a class="btn btn-outline" href="#" style="left:395px;top:1754px;width:160px;height:41px">Learn more <svg viewBox="0 0 16 16"><circle cx="8" cy="8" r="8" fill="#d56501"/><path d="M6 4l4 4-4 4" stroke="#fff" stroke-width="2" fill="none"/></svg></a>
<a class="btn btn-outline" href="#" style="left:646px;top:1754px;width:160px;height:41px">Learn more <svg viewBox="0 0 16 16"><circle cx="8" cy="8" r="8" fill="#d56501"/><path d="M6 4l4 4-4 4" stroke="#fff" stroke-width="2" fill="none"/></svg></a>
<a class="btn btn-outline" href="#" style="left:898px;top:1754px;width:160px;height:41px">Learn more <svg viewBox="0 0 16 16"><circle cx="8" cy="8" r="8" fill="#d56501"/><path d="M6 4l4 4-4 4" stroke="#fff" stroke-width="2" fill="none"/></svg></a>

<svg class="abs arrow" style="left:42px" viewBox="0 0 24 40"><path d="M20 4L4 20l16 16" stroke="#b3a9cf" stroke-width="3" fill="none"/></svg>
<svg class="abs arrow" style="left:1132px" viewBox="0 0 24 40"><path d="M4 4l16 16L4 36" stroke="#b3a9cf" stroke-width="3" fill="none"/></svg>

<!-- Clients -->
<h2 class="abs heading clients-title">OUR CLIENTS</h2>
<div class="card" style="left:110px"><p>Lorem ipsum dolor amet, consectetur adipiscing elit, sed do eiusmod tempor incididunt ut labore et dolore magna aliqua. Ut enim ad minim veniam,</p></div>
<div class="card" style="left:444px"><p>Lorem ipsum dolor amet, consectetur adipiscing elit, sed do eiusmod tempor incididunt ut labore et dolore magna aliqua. Ut enim ad minim veniam,</p></div>
<div class="card" style="left:778px"><p>Lorem ipsum dolor amet, consectetur adipiscing elit, sed do eiusmod tempor incididunt ut labore et dolore magna aliqua. Ut enim ad minim veniam,</p></div>
<div class="avatar" style="left:221px" role="img" aria-label="Client portrait photo"></div>
<div class="avatar" style="left:555px" role="img" aria-label="Client portrait photo"></div>
<div class="avatar" style="left:889px" role="img" aria-label="Client portrait photo"></div>
<div class="person" style="left:110px">Elin Marsh, <small>Chairman NKA</small></div>
<div class="person" style="left:444px">Nora Lindqvist, <small>Project Manager</small></div>
<div class="person" style="left:778px">Jonas Berg, <small>Chairman NKA</small></div>
<div class="stars" style="left:110px">★★★★★</div>
<div class="stars" style="left:444px">★★★★★</div>
<div class="stars" style="left:778px">★★★★★</div>

<!-- Request for quote -->
<svg class="abs quote" width="1200" height="660" viewBox="0 0 1200 660">
  <path d="M0 95L347 8L1200 108V556L855 649L0 543Z" fill="var(--orange)"/>
  <path d="M0 103L347 20L1200 118V545L855 636L0 534Z" fill="var(--olive)"/>
</svg>
<h2 class="abs heading quote-title">REQUEST FOR QUOTE</h2>
<p class="abs quote-text">Lorem ipsum dolor sit amet, consectetur adipiscing elit, sed do eiusmod tempor incididunt ut labore et dolore magna aliqua. Ut enim ad minim veniam, quis nostrud exercitation ullamco laboris nisi</p>
<a class="btn btn-solid" href="#" style="left:112px;top:2816px;width:154px;height:43px">Offerlink
  <svg viewBox="0 0 16 16"><circle cx="8" cy="8" r="8" fill="#fff"/><path d="M6 4l4 4-4 4" stroke="#d56501" stroke-width="2" fill="none"/></svg></a>
<div class="abs devices" role="img" aria-label="Tablet and phone showing finance dashboard charts"></div>

<!-- Footer -->
<div class="abs foot-brand"><span>Veltrana</span><i></i></div>
<span class="abs social" style="left:174px;background:#3b5998" aria-label="Social link"></span>
<span class="abs social" style="left:212px;background:#1da1f2" aria-label="Social link"></span>
<span class="abs social" style="left:251px;background:#db4437" aria-label="Social link"></span>
<span class="abs social" style="left:290px;background:#a23a9a" aria-label="Social link"></span>

<h4 class="abs foot-head" style="left:434px">Quick Links</h4>
<ul class="abs links"><li>Home</li><li>About Us</li><li>For entrepreneurs</li><li>GDPR</li><li>Start page</li><li>Contact Us</li></ul>

<h4 class="abs foot-head" style="left:631px">Contact Us</h4>
<div class="abs contact">
  <div class="row"><svg viewBox="0 0 16 16"><path d="M3 1l3 3-2 2c1 2 3 4 5 5l2-2 3 3-2 3C6 15 1 10 1 3z" fill="var(--gold)"/></svg><b>Phone</b>040-55 20 17</div>
  <div class="row"><svg viewBox="0 0 16 16"><rect x="1" y="3" width="14" height="10" fill="var(--gold)"/><path d="M1 3l7 6 7-6" stroke="#fff" fill="none"/></svg><b>Email</b>info@veltrana.se</div>
  <div class="row"><svg viewBox="0 0 16 16"><path d="M8 1a5 5 0 015 5c0 4-5 9-5 9S3 10 3 6a5 5 0 015-5z" fill="var(--gold)"/><circle cx="8" cy="6" r="2" fill="#fff"/></svg><b>Location</b>Veltrana AB Hamnvägen 12<br>211 22 Malmö</div>
</div>

<div class="abs partner"><i></i><span>Nordrevis</span></div>
<div class="abs rule"></div>
<p class="abs copyright">2020 Copyright - Veltrana | All Rights Reserved</p>
<a class="abs to-top" href="#" aria-label="Back to top"><svg width="14" height="14" viewBox="0 0 14 14"><path d="M2 9l5-5 5 5" stroke="#fff" stroke-width="2" fill="none"/></svg></a>

</body>
</html>
```